Outdoor sign for Brindle Auto Restoration

I need a horizontal 4'x 8' outdoor roadside sign for my classic auto restoration business. I have uploaded colors and our logo. Needs the Brindle name, a prominent Classic AUTO RESTORATION, phone number and website. We rebuild and restore vintage cars, trucks and 4x4s. I'd like something clean but possibly retro. Classic Auto Restoration is more important than the Brindle name. It needs to be visible and readable from the street. NO CLIP ART

Target Market(s)

Customers who need their vintage care restored or upgraded. Men and women ages 25-75

Industry/Entity Type

Automotive

Colors
FFC000
F8CF3A
FAE287
FDF2CF
FEFAEE

Requirements
Must have
• Legible. Bright. Readable as a backlit 4' x 8' large horizontal sign (roughly 120cm X 240cm)
Nice to have
• Use of the Brindle logo/type, Complete or Classic before prominent AUTO RESTORATION
Should not have
• Clip art of old cars or icons. And we don't want the Brindle Logo from the website because it wont be legible from the road. I have included the Illustrator file for Brindle text in the uploads

```html
<!DOCTYPE html>
<html lang="en">
<head>
<meta charset="utf-8">
<title>Brindle Auto Restoration – Roadside Sign</title>
<link rel="stylesheet" href="https://fonts.googleapis.com/css2?family=Oswald:wght@600&family=Playfair+Display:ital,wght@1,900&display=swap">
<style>
  :root {
    --sign-yellow: #F6AC1C;
    --ink: #231F20;
    --black: #000000;
    --cream: #FDF5D3;
    --page: #FFFFFF;
  }
  html, body {
    margin: 0;
    padding: 0;
    width: 1200px;
    height: 849px;
    overflow: hidden;
    background: var(--page);
  }
  .canvas {
    position: relative;
    width: 1200px;
    height: 849px;
  }
  .sign-art {
    position: absolute;
    left: 0;
    top: 0;
  }
  .brand-name {
    position: absolute;
    left: 292px;
    top: 262px;
    margin: 0;
    transform: translate(-50%, -50%) rotate(-30deg);
    font-family: "Oswald", sans-serif;
    font-weight: 600;
    font-size: 68px;
    letter-spacing: 2px;
    line-height: 1;
    color: var(--sign-yellow);
    text-transform: uppercase;
    white-space: nowrap;
  }
  .headline {
    position: absolute;
    margin: 0;
    font-family: "Playfair Display", serif;
    font-style: italic;
    font-weight: 900;
    line-height: 1;
    color: var(--ink);
    white-space: nowrap;
  }
  .headline-auto {
    right: 210px;
    top: 205px;
    font-size: 190px;
  }
  .headline-restoration {
    right: 170px;
    top: 395px;
    font-size: 138px;
  }
  .contact-bar {
    position: absolute;
    left: 172px;
    top: 607px;
    width: 864px;
    height: 75px;
    display: flex;
    align-items: center;
    font-family: "Playfair Display", serif;
    font-style: italic;
    font-weight: 900;
    font-size: 33px;
    font-variant-numeric: lining-nums;
    color: var(--ink);
  }
  .contact-web {
    position: absolute;
    left: 32px;
  }
  .contact-phone {
    position: absolute;
    left: 586px;
  }
</style>
</head>
<body>
<div class="canvas">
  <svg class="sign-art" width="1200" height="849" viewBox="0 0 1200 849" aria-hidden="true">
    <rect class="sign-frame" x="161" y="155" width="885" height="538" fill="var(--black)"/>
    <rect class="sign-field" x="167" y="161" width="873" height="526" fill="var(--sign-yellow)"/>
    <polygon class="corner-wedge" points="172,166 575,166 172,401" fill="var(--ink)"/>
    <rect class="contact-band" x="172" y="607" width="864" height="75" fill="var(--cream)"/>
  </svg>

  <p class="brand-name">Brindle</p>

  <h1 class="headline headline-auto">Auto</h1>
  <h1 class="headline headline-restoration">Restoration</h1>

  <div class="contact-bar">
    <span class="contact-web">brindleautoworks.com</span>
    <span class="contact-phone">501-555-0142</span>
  </div>
</div>
</body>
</html>
```